Velora Aesthetica

Medical doctor providing aesthetic medicine

* Double sided card
* Logo to be on card
Other details:
* Dr. Mirela Kostvan, BSc, MBChB, CCFP
* #214-215, 27903 83 Ave, Surrey, BC, V2T 4K7
* 604-718-2943
* info@veloraclinic.ca
* www.veloraclinic.ca

Industry/Entity Type

Medical / Health & Beauty

Contact Information for Business Card

see 'Project Description'

Colors
0054AA
0677BA
7BADD7
CADEEF
E8F1F8
FFF300
FFF600
FEFA6F
FFFEC7
FFFEE8

Requirements
Must have
• Modern, high-end design

```html
<!DOCTYPE html>
<html lang="en">
<head>
<meta charset="utf-8">
<title>Velora Aesthetica – Business Card</title>
<link rel="stylesheet" href="https://fonts.googleapis.com/css2?family=Montserrat:wght@400;500;700&display=swap">
<style>
  :root {
    --stage: #3a3a3a;
    --card: #131313;
    --card-back: #111111;
    --gold: #e6bd2a;
    --band: #f0c42c;
    --white: #ffffff;
    --pattern-dark: #1a1a1a;
    --pattern-light: #2a2a2a;
  }
  * { margin: 0; padding: 0; box-sizing: border-box; }
  html, body { width: 1200px; height: 900px; overflow: hidden; }
  body {
    background: var(--stage);
    font-family: "Montserrat", sans-serif;
    display: flex;
    flex-direction: column;
    align-items: center;
    justify-content: center;
    gap: 60px;
  }
  .card {
    position: relative;
    width: 630px;
    height: 360px;
    overflow: hidden;
    box-shadow: 0 18px 40px rgba(0,0,0,0.45);
  }

  /* Front */
  .card-front { background: var(--card); }
  .brand {
    position: absolute;
    left: 48px;
    top: 118px;
    width: 230px;
    display: flex;
    align-items: center;
    gap: 14px;
  }
  .brand-dot {
    flex: none;
    width: 18px;
    height: 18px;
    border-radius: 50%;
    background: var(--gold);
  }
  .brand-name {
    color: var(--white);
    font-weight: 500;
    font-size: 22px;
    letter-spacing: 0.14em;
    text-transform: uppercase;
    line-height: 1.3;
  }
  .divider {
    position: absolute;
    left: 300px;
    top: 40px;
    width: 1.5px;
    height: 240px;
    background: var(--gold);
  }
  .details {
    position: absolute;
    left: 330px;
    top: 70px;
    color: var(--white);
  }
  .doctor-name {
    color: var(--gold);
    font-weight: 700;
    font-size: 25px;
    line-height: 1.2;
  }
  .credentials {
    font-size: 15px;
    margin-top: 4px;
    margin-bottom: 26px;
  }
  .contact-list { list-style: none; }
  .contact-list li {
    display: flex;
    align-items: center;
    gap: 10px;
    font-size: 15px;
    line-height: 1.85;
  }
  .contact-icon { width: 14px; height: 14px; flex: none; }
  .address-band {
    position: absolute;
    left: 0;
    right: 0;
    bottom: 0;
    height: 40px;
    background: var(--band);
    color: var(--white);
    font-size: 15px;
    display: flex;
    align-items: center;
    padding-left: 48px;
  }

  /* Back */
  .card-back { background: var(--card-back); }
  .back-pattern {
    position: absolute;
    inset: 0;
    background: linear-gradient(120deg, var(--pattern-dark) 0%, var(--pattern-dark) 55%, var(--pattern-light) 100%);
  }
  .back-brand {
    position: absolute;
    left: 50%;
    top: 50%;
    transform: translate(-50%, -50%);
    display: flex;
    align-items: center;
    gap: 8px;
  }
  .back-brand .brand-dot { width: 10px; height: 10px; }
  .back-brand .brand-name {
    font-size: 12px;
    color: var(--gold);
  }
</style>
</head>
<body>

  <section class="card card-front">
    <div class="brand">
      <span class="brand-dot"></span>
      <span class="brand-name">Velora Aesthetica</span>
    </div>

    <div class="divider"></div>

    <div class="details">
      <p class="doctor-name">Dr. Mirela Kostvan</p>
      <p class="credentials">, BSc, MBChB, CCFP</p>
      <ul class="contact-list">
        <li>
          <svg class="contact-icon" viewBox="0 0 24 24" aria-hidden="true">
            <path fill="#e6bd2a" d="M6.6 10.8a15.1 15.1 0 0 0 6.6 6.6l2.2-2.2a1 1 0 0 1 1-.25 11.4 11.4 0 0 0 3.6.57 1 1 0 0 1 1 1V20a1 1 0 0 1-1 1A17 17 0 0 1 3 4a1 1 0 0 1 1-1h3.5a1 1 0 0 1 1 1c0 1.25.2 2.45.57 3.6a1 1 0 0 1-.25 1z"/>
          </svg>
          604-718-2943
        </li>
        <li>
          <svg class="contact-icon" viewBox="0 0 24 24" aria-hidden="true">
            <rect x="2" y="5" width="20" height="14" rx="1.5" fill="#e6bd2a"/>
            <path d="M3 6.5l9 6.5 9-6.5" fill="none" stroke="#131313" stroke-width="1.6"/>
          </svg>
          info@veloraclinic.ca
        </li>
        <li>
          <svg class="contact-icon" viewBox="0 0 24 24" aria-hidden="true">
            <circle cx="12" cy="12" r="10" fill="#e6bd2a"/>
            <path d="M2 12h20M12 2c3 3 3 17 0 20M12 2c-3 3-3 17 0 20" fill="none" stroke="#131313" stroke-width="1.4"/>
          </svg>
          www.veloraclinic.ca
        </li>
      </ul>
    </div>

    <div class="address-band">#214-215, 27903 83 Ave, Surrey, BC, V2T 4K7</div>
  </section>

  <section class="card card-back">
    <div class="back-pattern" role="img" aria-label="Tonal repeating pattern of the brand symbol across the card back"></div>
    <div class="back-brand">
      <span class="brand-dot"></span>
      <span class="brand-name">Velora Aesthetica</span>
    </div>
  </section>

</body>
</html>
```